Over 100 ladies will be traveling to Ocean City, MD for a Women's Retreat Conference. This flyer is for advertisement. This flyer is to circulate for registrations as well as to post on social media. Theme is Holy Spirit fire. I have attached a photo. All the information in the attachment should be included on the flyer. Information should be clearly readable end eye catching.

Target Market(s)

Church ladies

Industry/Entity Type

Religious

Font styles to use
Sans Serif

Colors

Designer to choose colors to be used in the design.

Requirements
Must have
• Title: Brightvale Womens Gathering 2019 "FIRE"
• All components in attachments

```html
<!DOCTYPE html>
<html lang="en">
<head>
<meta charset="utf-8">
<title>Brightvale Womens Gathering Fire 2019</title>
<link href="https://fonts.googleapis.com/css2?family=Catamaran:wght@400;500;600;700;800&display=swap" rel="stylesheet">
<style>
  :root {
    --royal: #0b4ba1;
    --flame: #f7a21b;
    --rose: #f24a6a;
    --violet: #4541b2;
    --url: #3c3aa6;
    --ink: #111111;
    --white: #ffffff;
  }
  * { margin: 0; padding: 0; box-sizing: border-box; }
  html, body { width: 887px; height: 1200px; overflow: hidden; background: var(--white); }
  body { font-family: "Catamaran", sans-serif; color: var(--ink); }
  .flyer { position: relative; width: 887px; height: 1200px; overflow: hidden; background: var(--white); }
  .flyer > * { position: absolute; }

  .side-bar { left: 0; top: 0; width: 51px; height: 470px; background: var(--royal); }

  .art-face { left: 400px; top: 0; width: 487px; height: 424px;
    background:
      radial-gradient(ellipse at 70% 35%, #2b3fc2 0%, rgba(60,70,200,.85) 25%, rgba(150,110,200,.5) 50%, rgba(255,255,255,0) 75%),
      radial-gradient(ellipse at 92% 15%, rgba(240,190,80,.8) 0%, rgba(240,120,130,.4) 30%, rgba(255,255,255,0) 55%),
      radial-gradient(ellipse at 85% 80%, rgba(200,120,190,.7) 0%, rgba(255,255,255,0) 55%); }

  .title { left: 105px; top: 72px; line-height: 1; }
  .title .brand { display: block; font-size: 48px; font-weight: 500; letter-spacing: -1.5px; color: var(--ink); }
  .title .headline { display: block; font-size: 64px; font-weight: 800; letter-spacing: -2.5px; color: var(--flame); line-height: 67px; margin-top: 6px; }

  .photo-snow { left: 0; top: 352px; width: 526px; height: 271px;
    background: linear-gradient(160deg, #c9cdd2 0%, #7f8890 45%, #3b4249 70%, #b9bec3 100%); }

  .photo-host { left: 526px; top: 380px; width: 144px; height: 216px;
    background: linear-gradient(180deg, #e8e3dc 0%, #c99870 45%, #e0506a 100%); }

  .host-band { left: 526px; top: 491px; width: 361px; height: 132px; background: var(--rose); }
  .host-label { left: 687px; top: 513px; font-size: 20px; font-weight: 500; letter-spacing: -.5px; color: var(--ink); }
  .host-name { left: 690px; top: 540px; font-size: 27px; font-weight: 800; font-style: italic; line-height: 32px; letter-spacing: -.5px; color: var(--white); }

  .speakers { left: 526px; top: 623px; width: 361px; height: 287px; background: var(--flame); }
  .speakers-label { left: 526px; top: 648px; width: 346px; text-align: center; font-size: 20px; font-weight: 500; letter-spacing: -.5px; color: var(--ink); }
  .speaker-photo { top: 709px; height: 129px; width: 113px; }
  .speaker-photo.one { left: 563px; background: linear-gradient(180deg, #d3d6d8 0%, #8a8d90 50%, #2a2a2a 100%); }
  .speaker-photo.two { left: 725px; width: 112px; background: linear-gradient(180deg, #f2f2f2 0%, #c8c8c8 45%, #1c1c1c 100%); }
  .speaker-name { top: 843px; width: 160px; text-align: center; font-size: 16px; font-weight: 800; letter-spacing: -.5px; line-height: 20px; }
  .speaker-name small { display: block; font-size: 14px; font-weight: 500; letter-spacing: 0; }
  .speaker-name.one { left: 540px; }
  .speaker-name.two { left: 700px; }

  .included { left: 99px; top: 638px; }
  .included h2 { font-size: 26px; font-weight: 800; letter-spacing: -.5px; color: var(--royal); line-height: 34px; }
  .included ul { list-style: none; margin-top: 2px; }
  .included li { position: relative; padding-left: 26px; font-size: 21px; font-weight: 500; letter-spacing: -.5px; line-height: 34px; }
  .included li::before { content: "-"; position: absolute; left: 0; }

  .cost { left: 99px; top: 808px; font-size: 43px; font-weight: 800; letter-spacing: -.5px; color: var(--royal); line-height: 50px; }
  .cost-note { left: 103px; top: 860px; font-size: 20px; font-weight: 500; letter-spacing: -.3px; }

  .policy { left: 0; top: 910px; width: 526px; height: 186px; background: var(--violet);
    padding: 13px 20px 0 60px; color: var(--white); font-size: 16px; font-weight: 500; line-height: 21px; letter-spacing: -.2px; }

  .hotel-photo { top: 910px; height: 79px; }
  .hotel-photo.outside { left: 526px; width: 134px; background: linear-gradient(180deg, #1b2c52 0%, #3b4c78 40%, #c57a4a 75%, #5a3a28 100%); }
  .hotel-photo.room { left: 660px; width: 117px; background: linear-gradient(180deg, #7ea8b8 0%, #d9dcd6 55%, #4e6d78 100%); }
  .hotel-photo.lobby { left: 777px; width: 110px; background: linear-gradient(180deg, #e9cf7a 0%, #d4a84c 55%, #f3efe6 100%); }

  .venue { left: 526px; top: 989px; width: 361px; height: 107px; background: var(--flame);
    padding-top: 11px; text-align: center; font-size: 21.5px; font-weight: 500; line-height: 26px; letter-spacing: -.3px; }

  .web { left: 0; top: 1120px; width: 887px; text-align: center; font-size: 31px; font-weight: 600; letter-spacing: 5px; color: var(--url); }
</style>
</head>
<body>
<main class="flyer">
  <div class="side-bar"></div>
  <div class="art-face" role="img" aria-label="Watercolour painting of a woman's face in blue, purple and gold splashes"></div>

  <h1 class="title">
    <span class="brand">Brightvale</span>
    <span class="headline">Womens</span>
    <span class="headline">Gathering</span>
    <span class="headline">Fire 2019</span>
  </h1>

  <div class="photo-snow" role="img" aria-label="Photo of a woman in a black hat looking over a snowy forest"></div>
  <div class="photo-host" role="img" aria-label="Portrait photo of the gathering host"></div>
  <div class="host-band"></div>
  <p class="host-label">Retreat Host:</p>
  <p class="host-name">Apostle Marla<br>Hensley</p>

  <div class="speakers"></div>
  <p class="speakers-label">Retreat Speakers:</p>
  <div class="speaker-photo one" role="img" aria-label="Portrait photo of Pastor Danita Moore"></div>
  <div class="speaker-photo two" role="img" aria-label="Portrait photo of Pastor Celeste Hardy"></div>
  <p class="speaker-name one">Pastor Danita Moore<small>Orlando, Florida</small></p>
  <p class="speaker-name two">Pastor Celeste Hardy<small>GLMI - Waldorf, Md.</small></p>

  <section class="included">
    <h2>Included:</h2>
    <ul>
      <li>All Retreat Sessions</li>
      <li>2 Nights Hotel Accommodations</li>
      <li>1 Hot Lunch Buffet</li>
      <li>1 Full Hot American Breakfast</li>
    </ul>
  </section>
  <p class="cost">Cost:&nbsp; $295</p>
  <p class="cost-note">*Based on double occupancy</p>

  <p class="policy">**ALL deposits/registrations are NON-refundable and NON-transferable. Your entire registration is due by October 1, 2018. Please submit your desired roommate's name at the time of registration. If you do not choose a roommate one will be assigned to you unless you have registered for a private room. Please contact Rena via email rena@brightvaleministries.com or phone 240-555-0147 for more information.</p>

  <div class="hotel-photo outside" role="img" aria-label="Photo of the hotel exterior at night"></div>
  <div class="hotel-photo room" role="img" aria-label="Photo of a hotel guest room"></div>
  <div class="hotel-photo lobby" role="img" aria-label="Photo of the hotel lobby staircase"></div>
  <address class="venue" style="font-style:normal">Seaside Crest Hotel &amp; Suites<br>1450 Harbor Ave.<br>Ocean City, Maryland 21842</address>

  <p class="web">brightvale2019.eventreg.com</p>
</main>
</body>
</html>
```